Mortgage Broker Site

Need a custom design for a mortgage broker site - please refer to the attached Word .doc that gives more detail.

Number of Pages Required

5+ page

Colors

Designer to choose colors to be used in the design.

```html
<!DOCTYPE html>
<html lang="en">
<head>
<meta charset="utf-8">
<title>Hearthline Mortgage</title>
<link href="https://fonts.googleapis.com/css2?family=Roboto:wght@400;500;700&display=swap" rel="stylesheet">
<style>
:root{
  --brand:#9b0a1f;
  --white:#ffffff;
  --ink:#111111;
  --muted:#555555;
  --footer:#3598db;
  --skyline:#e6e7ea;
}
*{box-sizing:border-box;margin:0;padding:0}
html,body{width:750px;height:1200px;overflow:hidden;background:var(--white)}
body{position:relative;font-family:'Roboto',sans-serif;color:var(--ink)}
.abs{position:absolute}
/* hero */
.hero{left:0;top:0;width:750px;height:371px;overflow:hidden}
.hero-photo{position:absolute;inset:0;background:linear-gradient(100deg,#8f7b72 0%,#9c8c86 30%,#6f6a77 55%,#77748a 75%,#8a8a98 100%)}
.hero-shade{position:absolute;inset:0;background:rgba(40,35,55,.35)}
.brand-name{left:40px;top:14px;font-size:24px;font-weight:500;color:var(--white);display:flex;align-items:center;gap:5px}
.brand-name .dot{width:8px;height:8px;background:var(--brand)}
.nav{top:20px;display:flex;font-size:7px;font-weight:500;color:var(--white);letter-spacing:.1px}
.nav a{position:absolute;color:var(--white);text-decoration:none;white-space:nowrap}
.btn{display:flex;align-items:center;justify-content:center;font-size:6.5px;font-weight:700;letter-spacing:.1px}
.btn-red{background:var(--brand);color:var(--white)}
.btn-white{background:var(--white);color:var(--brand)}
.hero h1{left:344px;top:128px;font-size:26.5px;font-weight:700;line-height:31px;color:var(--white)}
.hero p{left:344px;top:196px;width:280px;font-size:7.4px;line-height:13.3px;font-weight:500;color:var(--white)}
/* tools */
.tools-title{left:0;width:750px;top:421px;text-align:center;font-size:15px;font-weight:700}
.tools-bar{left:310px;top:441px;width:130px;height:2px;background:var(--brand)}
.tools-sub{left:250px;width:250px;top:453px;text-align:center;font-size:7px;line-height:12px;color:#333}
.diamond{width:98px;height:98px;background:var(--white);transform:rotate(45deg);box-shadow:0 0 12px rgba(0,0,0,.08)}
.tool-art{width:46px;height:46px;border-radius:6px}
.tool-name{width:180px;text-align:center;font-size:10.5px;font-weight:700}
.tool-desc{width:180px;text-align:center;font-size:7px;line-height:12.6px;color:var(--muted)}
/* limits */
.limits{left:0;top:715px;width:750px;height:175px;background:linear-gradient(110deg,#8d8580 0%,#6f5a53 40%,#6a4c48 60%,#5c5a62 100%)}
.limits-shade{position:absolute;inset:0;background:rgba(30,25,30,.35)}
.limits h2{position:absolute;left:0;width:750px;top:40px;text-align:center;font-size:13.6px;font-weight:700;color:var(--white)}
.limits p{position:absolute;left:120px;width:510px;top:67px;text-align:center;font-size:10px;line-height:17px;color:var(--white)}
.search{position:absolute;left:258px;top:117px;width:234px;height:20px;background:var(--white);border:1px solid var(--white);display:flex}
.search span{margin-left:auto;width:61px;height:18px;background:var(--brand);color:var(--white);font-size:6.5px;font-weight:700;display:flex;align-items:center;justify-content:center}
/* connect */
.skyline{left:0;top:940px;width:750px;height:80px;background:linear-gradient(180deg,#f4f4f6 0%,var(--skyline) 100%)}
.connect-title{left:0;width:750px;top:929px;text-align:center;font-size:13.6px;font-weight:700}
/* footer */
.footer{left:0;top:1020px;width:750px;height:180px;background:var(--footer);color:var(--white)}
.footer .brand-name{left:125px;top:34px;font-size:25px}
.social{position:absolute;top:78px;width:12px;height:12px;border:1px solid rgba(255,255,255,.8)}
.col{position:absolute;top:30px;font-size:6px;line-height:12.5px}
.col h4{font-size:6.8px;font-weight:700;margin-bottom:1px}
.rule{position:absolute;left:125px;top:118px;width:500px;height:1px;background:rgba(255,255,255,.5)}
.legal{position:absolute;left:125px;width:470px;font-size:6px;line-height:8px}
.to-top{position:absolute;left:602px;top:140px;width:23px;height:23px;background:var(--white)}
</style>
</head>
<body>

<section class="abs hero">
  <div class="hero-photo" role="img" aria-label="Photo of a smiling family of three sitting together on a sofa at home"></div>
  <div class="hero-shade"></div>
  <div class="abs brand-name"><span>Hearthline</span><span class="dot"></span></div>
  <nav class="abs nav" style="left:0;width:750px">
    <a style="left:367px">RATES</a>
    <a style="left:410px">PURCHASE</a>
    <a style="left:467px">REFINANCE</a>
    <a style="left:525px">SCHEDULE A CALL</a>
    <a style="left:606px">GUIDES</a>
  </nav>
  <div class="abs btn btn-red" style="left:650px;top:15px;width:60px;height:19px">APPLY NOW</div>
  <h1 class="abs">MORTGAGE RATES ARE<br>AT ALL TIME LOWS!</h1>
  <p class="abs">Lorem ipsum dolor sit amet, consectetuer adipiscing elit, sed diam nonummy nibh euismod tincidunt ut laoreet dolore magna Ut wisi enim ad minim veniam suscipit lobortis aliquam erat volutpat.</p>
  <div class="abs btn btn-red" style="left:343px;top:251px;width:79px;height:19px">PURCHASE RATES</div>
  <div class="abs btn btn-white" style="left:433px;top:251px;width:79px;height:19px">REFINANCE RATES</div>
  <svg class="abs" style="left:367px;top:336px" width="16" height="25" viewBox="0 0 16 25">
    <rect x="1" y="1" width="14" height="23" rx="7" fill="none" stroke="#fff" stroke-width="1"/>
    <line x1="8" y1="13" x2="8" y2="18" stroke="#fff" stroke-width="1"/>
  </svg>
</section>

<h2 class="abs tools-title">MORTGAGE TOOLS</h2>
<div class="abs tools-bar"></div>
<p class="abs tools-sub">Duis autem vel eum iriure dolor in hendrerit in vulputate velit esse molestie consequat, vel illum dolore eu feugiat</p>

<div class="abs diamond" style="left:236px;top:508px"></div>
<div class="abs tool-art" role="img" aria-label="Illustration of hands holding a small house" style="left:262px;top:530px;background:linear-gradient(135deg,#f3c9a0,#9fc3e0)"></div>
<div class="abs tool-name" style="left:192px;top:636px">Mortgage&nbsp; Claculator</div>
<div class="abs tool-desc" style="left:195px;top:654px">See how much you can afford by home Price,mothly payment, or income</div>

<div class="abs diamond" style="left:416px;top:508px"></div>
<div class="abs tool-art" role="img" aria-label="Illustration of a house with a magnifying glass and location pin" style="left:442px;top:530px;background:linear-gradient(135deg,#e8e3dc,#c9333a 70%,#6aa84f)"></div>
<div class="abs tool-name" style="left:375px;top:636px">Home Value Checker</div>
<div class="abs tool-desc" style="left:375px;top:652px">Should you refinance? This calculator breaks down monthly and lifetime cost</div>

<section class="abs limits" role="img" aria-label="Photo of a calculator beside a small model house and paperwork">
  <div class="limits-shade"></div>
  <h2>2019 MORTGAGE LOAN LIMITS FOR CONVENTIONAL, FHA, &amp; VA LOANS</h2>
  <p>Mortgage loan limits for every U.S. county, as published by Homestead Trust &amp; Keystone Mortgage Corp, the Federal Housing Administration (FHA), and the Department of Veterans Affairs (VA)</p>
  <div class="search"><span>SEARCH</span></div>
</section>

<div class="abs skyline" role="img" aria-label="Faint illustration of a city skyline"></div>
<h2 class="abs connect-title">Connect With America’s Lending Experts Today!</h2>
<div class="abs btn btn-red" style="left:336px;top:961px;width:79px;height:19px">(555) 014-2270</div>

<footer class="abs footer">
  <div class="abs brand-name"><span>Hearthline</span><span class="dot"></span></div>
  <span class="social" style="left:138px"></span>
  <span class="social" style="left:155px"></span>
  <span class="social" style="left:171px"></span>
  <span class="social" style="left:187px"></span>
  <div class="col" style="left:285px"><h4>LINKS</h4>Get a Mortgage Rate Now<br>Loan Types<br>Hearthline Disclosures<br>Conforming, VA &amp; FHA Loan Limits</div>
  <div class="col" style="left:458px"><h4>COMPANY</h4>About Us<br>Careers<br>Hearthline Resources<br>Contact</div>
  <div class="col" style="left:584px"><h4>POLICIES</h4>Security Policy<br>Privacy Policy<br>Terms of Use<br>Email Policy</div>
  <div class="rule"></div>
  <p class="legal" style="top:140px">Hearthline NMLS #418203. Click here to view our licensing with the NMLS and DRE</p>
  <p class="legal" style="top:155px">2020 Copyright ©Hearthline, Inc. All rights reserved. Lending services provided by Hearthline, Inc dba Hearthline. Rates, program terms and conditions are subject to change without notice.</p>
  <svg class="to-top" viewBox="0 0 23 23">
    <path d="M11.5 6 L16 11 H13 V17 H10 V11 H7 Z" fill="#111"/>
  </svg>
</footer>

</body>
</html>
```